Scrum Master & Agile IT Coach Needing Business Website

Hello, my name is Brent Ellison
I am a project manger, scrum master, & agile coach. I work with IT development teams on major projects for Fortune 500 companies . My project management business has a website and can be found here: www.tq-steadfast.example

I have launched a new company, ALL focused on IT Agile Coaching, I am looking to have a website created for my new company - the name of the new company is: Pins and Pegs - Agile IT Coaching and Training.
I have a logo and it is provided in the materials. I like to logo; I am open to different color pallets.

The website will have a total of 7 pages; I have content for 5 of the 7 pages prepared; the other 2 pages will say under construction.

Page 1 Who am I, What I do, My Experience
Demonstrated experience and progression from Scrum Master to
Program Manager to Coach

Page 2 Pins & Pegs - Agile Team Coaching
teams working major IT projects, multiple months/years

Page 3 Coaching @ the Team Level

Page 4 Coaching @ the Program Level ; ScaledFlow ART level

Pages 5 -6 Under Construction

Page 7 Presentations, Slide Decks, Reference Materials

Mentors Nook need to have this highlighted somewhere Monthly Blog
Updates

Industry/Entity Type

IT development

Coding

Coded - Design and coding required

Number of Pages Required

5+ page

Requirements
Must have
• the website must be bold - I want those who visit to remember coming to my coaching site
Nice to have
• nice to have will be a modern / futuristic website; I work with IT developers, I want a website they will like
Should not have
• should not be stiff - it should be professional but fun

```html
<!DOCTYPE html>
<html lang="en">
<head>
<meta charset="utf-8">
<title>Pins &amp; Pegs - Agile IT Coaching and Training</title>
<link href="https://fonts.googleapis.com/css2?family=Poppins:wght@300;400;500;600;700;800&display=swap" rel="stylesheet">
<style>
:root{
  --navy:#1a4f93;
  --bright:#1f6fd8;
  --ink:#222831;
  --muted:#555b66;
  --hero:#1c2029;
  --soft:#f2f3f5;
  --white:#ffffff;
  --rule:#bfc4cc;
}
*{box-sizing:border-box;margin:0;padding:0}
html,body{width:1200px;height:4493px;overflow:hidden}
body{position:relative;font-family:'Poppins',sans-serif;color:var(--ink);background:var(--white)}
.abs{position:absolute}
.btn{position:absolute;display:inline-block;background:var(--bright);color:var(--white);font-weight:700;font-size:15px;border-radius:10px;text-align:center;line-height:46px;height:46px;text-decoration:none;box-shadow:0 4px 10px rgba(0,0,0,.15)}

/* hero */
.hero{left:0;top:0;width:1200px;height:680px;background:linear-gradient(120deg,#3a3f4a 0%,#262a33 45%,#14171d 100%);border-bottom-right-radius:230px 340px;overflow:hidden}
.topbar{left:100px;top:8px;width:1000px;height:24px;color:#fff;font-size:15px}
.social{display:flex;gap:14px;position:absolute;left:0;top:4px}
.social span{width:14px;height:14px;border-radius:50%;background:#fff;display:block}
.contact-top{position:absolute;right:0;top:0;display:flex;gap:16px;align-items:center}
.contact-top svg{vertical-align:-2px;margin-right:4px}
.brand{display:flex;align-items:center;gap:12px;color:#fff;font-weight:800;font-size:34px;letter-spacing:.5px}
.brand i{width:34px;height:34px;border:3px solid #fff;display:block}
.nav{left:440px;top:74px;display:flex;gap:26px;color:#fff;font-size:15px;font-weight:500}
.welcome{left:178px;top:258px;color:#fff;font-size:26px;letter-spacing:10px;font-weight:400}
.hero-title{left:176px;top:300px;color:#fff;font-size:80px;font-weight:800;letter-spacing:2px}

/* about */
.about-h{left:98px;top:790px;font-size:45px;line-height:56px;font-weight:400}
.about-h b{color:var(--bright);font-weight:700}
.about-sub{left:100px;top:910px;width:500px;font-size:22px;line-height:31px;font-weight:600;color:#333}
.about-p{left:98px;top:1025px;width:480px;font-size:16px;line-height:29px;color:var(--muted)}
.portrait{left:672px;top:740px;width:428px;height:428px;border-radius:50% 0 50% 50%;background:linear-gradient(160deg,#9a8a7e 0%,#6e5748 45%,#3f3530 100%)}
.name{left:672px;top:1188px;width:428px;text-align:center;font-size:18px;letter-spacing:5px;font-weight:700}
.role{left:672px;top:1225px;width:428px;text-align:center;font-size:15px;font-weight:500}

/* partners */
.partners{left:0;top:1308px;width:1200px;height:612px;background:var(--navy);border-top-left-radius:200px 165px}
.pcard{position:absolute;top:141px;width:316px}
.pcard .ph{height:262px;border-radius:8px;background:linear-gradient(180deg,#eef1f5 0%,#cfd6de 55%,#4a5566 100%)}
.pcard h3{margin-top:22px;text-align:center;color:#fff;font-size:21px;font-weight:600}
.pcard .btn{position:relative;display:block;width:166px;margin:22px auto 0;font-size:14px}

/* designations */
.des-title{left:0;top:1950px;width:1200px;text-align:center;font-size:45px;font-weight:400}
.des-title b{color:var(--bright);font-weight:700}
.des-item{position:absolute;width:464px;height:136px;display:flex;align-items:center}
.des-item.rule{border-bottom:2px solid var(--rule)}
.badge{width:130px;height:130px;border-radius:50%;flex:none}
.badge.gold{background:radial-gradient(circle,#f9b233,#e98a16)}
.badge.navy{background:#1d3f6e;border-radius:14px;transform:rotate(45deg) scale(.72)}
.badge.blue{background:radial-gradient(circle,#2aa9e0,#1681c2)}
.badge.ring{background:#fff;border:5px solid #1d3f6e;transform:scale(.78)}
.des-item p{margin-left:36px;font-size:16px;font-weight:600;line-height:24px}

/* roles */
.roles{left:0;top:2504px;width:1200px;height:572px;background:var(--navy);border-top-right-radius:220px 165px}
.roles-img{left:117px;top:96px;width:408px;height:405px;border-radius:50% 0 50% 50%;background:linear-gradient(135deg,#e4e8ed,#a9b2bd 55%,#5d6672)}
.roles h2{position:absolute;left:610px;top:160px;color:#fff;font-size:45px;font-weight:400}
.roles h2 b{font-weight:700}
.roles ul{position:absolute;left:610px;top:240px;width:470px;list-style:none;color:#fff;font-size:19px;line-height:26px}
.roles li{position:relative;padding-left:20px;margin-bottom:27px}
.roles li:before{content:"";position:absolute;left:0;top:8px;border-left:8px solid #fff;border-top:5px solid transparent;border-bottom:5px solid transparent}

/* experience */
.exp-bg{left:0;top:3620px;width:1200px;height:470px;background:var(--soft)}
.exp-title{left:0;top:3115px;width:1200px;text-align:center;font-size:45px;font-weight:400}
.exp-title b{color:var(--bright);font-weight:700}
.ecard{position:absolute;top:3258px;width:313px;height:614px;background:var(--navy);color:#fff;text-align:center;padding:100px 20px 0}
.ecard .ico{position:absolute;left:50%;top:-66px;margin-left:-66px;width:132px;height:132px;border-radius:50%;background:var(--bright);border:6px solid #fff;display:flex;align-items:center;justify-content:center}
.ecard h3{font-size:21px;font-weight:600;line-height:32px;margin-bottom:10px}
.ecard ul{list-style:none;font-size:16px;line-height:24px}
.ecard li{margin-bottom:7px}
.ecard li:before{content:"\2714 ";font-weight:700}

/* cta */
.cta-h{left:234px;top:3926px;font-size:45px;line-height:54px;font-weight:400}
.cta-h b{color:var(--bright);font-weight:700}

/* footer */
.footer{left:0;top:4081px;width:1200px;height:412px;background:var(--navy);border-top-left-radius:105px 105px;color:#fff}
.footer .brand{position:absolute;left:99px;top:150px;font-size:40px}
.footer .brand i{width:40px;height:40px}
.fsocial{position:absolute;left:252px;top:262px;display:flex;gap:22px}
.fsocial span{width:18px;height:18px;border-radius:50%;background:#fff;display:block}
.fcol{position:absolute;top:60px;font-size:16px}
.fcol h4{color:#3f9bff;font-size:18px;font-weight:500;margin-bottom:20px}
.fcol li{list-style:none;line-height:34px}
.fcol.links li:before{content:"\203A";margin-right:10px}
.fcol.contact li{display:flex;gap:10px;line-height:24px;margin-bottom:10px}
.frule{position:absolute;left:99px;top:352px;width:1002px;border-top:1px solid rgba(255,255,255,.3)}
.copy{position:absolute;left:0;top:372px;width:1200px;text-align:center;font-size:14px;color:#dbe3ee}
</style>
</head>
<body>

<section class="abs hero" role="img" aria-label="Dark photo of hands typing on a laptop with program code in the background">
  <div class="abs topbar">
    <div class="social"><span></span><span></span><span></span></div>
    <div class="contact-top">
      <span><svg width="13" height="13" viewBox="0 0 24 24"><path fill="#fff" d="M6.6 10.8a15 15 0 0 0 6.6 6.6l2.2-2.2c.3-.3.7-.4 1-.2 1.1.4 2.3.6 3.6.6.6 0 1 .4 1 1V20c0 .6-.4 1-1 1A17 17 0 0 1 3 4c0-.6.4-1 1-1h3.5c.6 0 1 .4 1 1 0 1.3.2 2.5.6 3.6.1.3 0 .7-.2 1z"/></svg>1800 555 0199</span>
      <span><svg width="14" height="11" viewBox="0 0 24 18"><path fill="#fff" d="M0 0h24v18H0zM12 10 2 2v1l10 8 10-8V2z"/></svg>info@pinsandpegs.example</span>
    </div>
  </div>
  <div class="abs brand" style="left:105px;top:58px"><i></i>Pins &amp; Pegs</div>
  <nav class="abs nav"><span>Who am I</span><span>Pins &amp; Pegs</span><span>The Team Level</span><span>Coaching</span><span>Presentations</span><span>Monthly Blog</span></nav>
  <svg class="abs" style="left:98px;top:305px" width="34" height="64" viewBox="0 0 34 64"><path d="M32 2 2 32l30 30" fill="none" stroke="#fff" stroke-width="2"/></svg>
  <svg class="abs" style="left:1070px;top:305px" width="34" height="64" viewBox="0 0 34 64"><path d="M2 2l30 30L2 62" fill="none" stroke="#fff" stroke-width="2"/></svg>
  <p class="abs welcome">WELCOME TO</p>
  <h1 class="abs hero-title">PINS &amp; PEGS</h1>
  <a class="btn" style="left:178px;top:417px;width:164px">GET IN TOUCH</a>
</section>

<h2 class="abs about-h">Who am I, What I do,<br><b>My Experience</b></h2>
<p class="abs about-sub">Demonstrate experience and progression from Scrum Master to Program Manager to Coach</p>
<p class="abs about-p">Brent Ellison is the Owner of Steadfast Quality Projects, LLC and serves as Principal Lead Consultant on waterfall and agile contract opportunities.</p>
<a class="btn" style="left:98px;top:1138px;width:166px">KNOW MORE</a>
<div class="abs portrait" role="img" aria-label="Portrait photo of Brent Ellison"></div>
<p class="abs name">BRENT ELLISON</p>
<p class="abs role">Senior Scrum Master &amp; Team Agile Coach</p>

<section class="abs partners">
  <div class="pcard" style="left:99px"><div class="ph" role="img" aria-label="Photo of a coach in a business suit in an office"></div><h3>Agile Guild Council</h3><a class="btn">VIEW DETAILS</a></div>
  <div class="pcard" style="left:442px"><div class="ph" role="img" aria-label="Photo of a coach in a business suit"></div><h3>Badgeway</h3><a class="btn">VIEW DETAILS</a></div>
  <div class="pcard" style="left:786px"><div class="ph" role="img" aria-label="Photo of a coach holding a phone"></div><h3>Scaled Flow Alliance</h3><a class="btn">VIEW DETAILS</a></div>
</section>

<h2 class="abs des-title">Coaching <b>Designations</b></h2>
<div class="des-item rule" style="left:99px;top:2036px"><div class="badge gold"></div><p>A-CFP</p></div>
<div class="des-item rule" style="left:99px;top:2172px"><div class="badge gold" style="background:radial-gradient(circle,#f6a04a,#e2701d)"></div><p>Certified Flow Foundations<br>Educator</p></div>
<div class="des-item" style="left:99px;top:2308px"><div class="badge blue"></div><p>CFP-SP</p></div>
<div class="des-item rule" style="left:638px;top:2036px"><div class="badge navy"></div><p>ScaledFlow Advanced Scrum<br>Master</p></div>
<div class="des-item" style="left:638px;top:2172px"><div class="badge ring"></div><p>IAG-TCC</p></div>

<section class="abs roles">
  <div class="abs roles-img" role="img" aria-label="Photo of hands working on a laptop and tablet"></div>
  <h2>Roles I <b>Have Held</b></h2>
  <ul>
    <li>Sr. Scrum Master</li>
    <li>Advanced ScaledFlow Scrum Master</li>
    <li>Hybrid Scrum Master/ Project Manager</li>
    <li>Business (Finance Transformation Program Manager</li>
  </ul>
</section>

<div class="abs exp-bg"></div>
<h2 class="abs exp-title">What is my <b>Experience</b></h2>
<div class="ecard" style="left:99px">
  <div class="ico"><svg width="56" height="56" viewBox="0 0 56 56" fill="none" stroke="#fff" stroke-width="2"><rect x="16" y="6" width="24" height="44" rx="3"/><path d="M23 24l-4 4 4 4M33 24l4 4-4 4M30 22l-4 12"/></svg></div>
  <h3>As a ScaledFlow Adv Scrum Master, I</h3>
  <ul><li>Stand up teams</li><li>Run development</li><li>Efforts concurrently leading multiple teams</li><li>Run ScaledFlow ceremonies</li><li>Scrum of Scrums facilitator</li><li>PI Planning team facilitator (multiple teams on ART)</li><li>Teach and coach to advanced development team strategies</li><li>Lead program level communications and business status updates on behalf of the team</li></ul>
</div>
<div class="ecard" style="left:443px">
  <div class="ico"><svg width="56" height="56" viewBox="0 0 56 56" fill="none" stroke="#fff" stroke-width="2"><rect x="6" y="10" width="44" height="36" rx="4"/><path d="M6 18h44M24 26l-5 5 5 5M32 26l5 5-5 5"/></svg></div>
  <h3>As a Hybrid Scrum Master / Project Manager, I</h3>
  <ul><li>Standup teams</li><li>Run multiple program level projects simultaneously</li><li>Implement custom hybrid</li><li>Development strategies</li><li>Manage to project triple constraints</li><li>Communications lead and business liaison</li><li>Use multiple coaching styles based on team and project</li></ul>
</div>
<div class="ecard" style="left:788px">
  <div class="ico"><svg width="56" height="56" viewBox="0 0 56 56" fill="none" stroke="#fff" stroke-width="2"><circle cx="28" cy="20" r="9"/><path d="M10 50V30h10v20M23 50V34h10v16M36 50V28h10v22M6 50h44"/></svg></div>
  <h3>Business Transformation Program Manager</h3>
  <ul><li>Lead business transformation efforts at the program level</li><li>Work with multiple product owners, business analysts, and business stakeholders on requirements</li><li>Lead the international rollout, Onboarding, and support of new multi-functional CloudCRM tool</li><li>Standup and lead multi-functional teams consisting of business and technology team members</li><li>Serve as program organization and communications lead</li></ul>
</div>

<h2 class="abs cta-h">Where does Coaching<br><b>Come in to Play</b></h2>
<a class="btn" style="left:760px;top:3966px;width:203px;height:48px;line-height:48px;border-radius:14px">GET IN TOUCH</a>

<footer class="abs footer">
  <div class="brand"><i></i>Pins &amp; Pegs</div>
  <div class="fsocial"><span></span><span></span><span></span></div>
  <div class="fcol links" style="left:577px"><h4>Quick Links</h4><ul><li>Who am I</li><li>Pins &amp; Pegs</li><li>The Team Level</li><li>Coaching</li><li>Presentations</li><li>Monthly Blog</li></ul></div>
  <div class="fcol contact" style="left:889px;width:230px"><h4>Contact Us</h4><ul>
    <li><svg width="14" height="14" viewBox="0 0 24 24"><path fill="#fff" d="M6.6 10.8a15 15 0 0 0 6.6 6.6l2.2-2.2c.3-.3.7-.4 1-.2 1.1.4 2.3.6 3.6.6.6 0 1 .4 1 1V20c0 .6-.4 1-1 1A17 17 0 0 1 3 4c0-.6.4-1 1-1h3.5c.6 0 1 .4 1 1 0 1.3.2 2.5.6 3.6.1.3 0 .7-.2 1z"/></svg>1800 555 0199</li>
    <li><svg width="14" height="12" viewBox="0 0 24 18"><path fill="#fff" d="M0 0h24v18H0zM12 10 2 2v1l10 8 10-8V2z"/></svg>info@pinsandpegs.example</li>
    <li><svg width="14" height="18" viewBox="0 0 24 32"><path fill="#fff" d="M12 0a12 12 0 0 0-12 12c0 9 12 20 12 20s12-11 12-20A12 12 0 0 0 12 0zm0 17a5 5 0 1 1 0-10 5 5 0 0 1 0 10z"/></svg>12 Harbor Lane, Suite 200</li>
  </ul></div>
  <div class="frule"></div>
  <p class="copy">© 2022 Pins &amp; Pegs. All right reserved</p>
</footer>

</body>
</html>
```